BRIARWOOD LOUNGE FRIDAY MAY 3

Flyer design for bar/nightclub event. Trying to keep a general theme with their flyers (see below) but would like to add some neon or some pop to it.

TEXT:

Briarwood Bar & Lounge Presents

LANTERN NIGHTS
GRAND OPENING EVENT

PURE HOUSE MUSIC W/

VORTEX
MARCO TELLEN
BRANDT & DJ WOBNIX

21+
9PM-130AM
712 K AVENUE DAVIS CA

Target Market(s)

House/dance music crowd.

Industry/Entity Type

Night Club

Font styles to use
Sans Serif

Colors
9bcb3c
fbee3d
ffffff

Requirements
Must have
• Large DJ names
Nice to have
• General theme of the attached flyers. Neon colors that stick with the theme. Anything else that looks cool will be considered

```html
<!DOCTYPE html>
<html lang="en">
<head>
<meta charset="utf-8">
<title>Lantern Nights – Briarwood Bar &amp; Lounge</title>
<link rel="stylesheet" href="https://fonts.googleapis.com/css2?family=Dancing+Script:wght@700&family=Montserrat:wght@500;600;700;800&display=swap">
<style>
  :root {
    --page-bg: #e9eaec;
    --flyer-black: #050303;
    --brand-green: #2f3b1f;
    --brand-gold: #d9b52c;
    --neon-yellow: #fbee3d;
    --neon-green: #9bcb3c;
    --white: #ffffff;
    --flame-deep: #7a1b05;
    --flame-mid: #d9480f;
    --flame-bright: #ff9a1f;
    --flame-glow: #ffd23a;
  }
  * { box-sizing: border-box; margin: 0; padding: 0; }
  html, body { width: 1200px; height: 810px; overflow: hidden; }
  body {
    background: var(--page-bg);
    font-family: "Montserrat", Arial, sans-serif;
    position: relative;
  }
  .flyer {
    position: absolute;
    left: 332px; top: 25px;
    width: 536px; height: 760px;
    background: var(--flyer-black);
    overflow: hidden;
  }
  .flame-field {
    position: absolute;
    left: 0; top: 200px; width: 536px; height: 400px;
    background:
      radial-gradient(ellipse 38% 45% at 55% 80%, var(--flame-bright) 0%, var(--flame-mid) 40%, rgba(122,27,5,0.6) 70%, transparent 100%),
      radial-gradient(ellipse 30% 40% at 25% 85%, var(--flame-mid) 0%, rgba(122,27,5,0.5) 60%, transparent 100%),
      radial-gradient(ellipse 25% 45% at 85% 75%, var(--flame-mid) 0%, rgba(122,27,5,0.4) 60%, transparent 100%),
      radial-gradient(ellipse 50% 55% at 50% 40%, rgba(122,27,5,0.55) 0%, transparent 80%);
  }
  .flame-strip {
    position: absolute;
    left: 0; bottom: 0; width: 536px; height: 62px;
    background:
      radial-gradient(ellipse 60% 90% at 30% 100%, var(--flame-glow) 0%, transparent 80%),
      linear-gradient(to bottom, var(--flyer-black) 0%, var(--flame-deep) 25%, var(--flame-mid) 55%, var(--flame-bright) 100%);
  }
  .brand {
    position: absolute;
    left: 173px; top: 34px; width: 190px; height: 54px;
    border: 2px solid var(--brand-gold);
    background: var(--brand-green);
    display: flex; align-items: center; justify-content: center; gap: 8px;
  }
  .brand-mark {
    width: 14px; height: 14px;
    background: var(--brand-gold);
  }
  .brand-name {
    color: var(--white);
    font-weight: 700;
    font-size: 12.5px;
    letter-spacing: 0.02em;
  }
  .event-title {
    position: absolute;
    left: 0; top: 92px; width: 536px; height: 300px;
    overflow: visible;
  }
  .event-title text {
    font-family: "Dancing Script", cursive;
    font-weight: 700;
    fill: url(#flameFill);
    stroke: var(--white);
    stroke-width: 5px;
    paint-order: stroke;
  }
  .event-tagline {
    position: absolute;
    left: 0; top: 400px; width: 536px;
    text-align: center;
    color: var(--white);
    font-size: 13px;
    font-weight: 600;
    letter-spacing: 0.04em;
  }
  .age-badge {
    position: absolute;
    left: 38px; top: 470px;
    width: 70px; height: 70px;
    border-radius: 50%;
    border: 3px solid var(--neon-green);
    box-shadow: 0 0 12px var(--neon-green), inset 0 0 8px var(--neon-green);
    color: var(--neon-green);
    font-size: 24px;
    font-weight: 800;
    display: flex; align-items: center; justify-content: center;
  }
  .hours-badge {
    position: absolute;
    left: 392px; top: 458px;
    width: 108px; height: 108px;
    border-radius: 50%;
    background: var(--neon-yellow);
    border: 2px solid var(--flyer-black);
    box-shadow: 0 0 0 1px var(--neon-yellow);
    display: flex; flex-direction: column; align-items: center; justify-content: center;
    color: var(--flyer-black);
    font-weight: 700;
    line-height: 1.1;
    transform: rotate(-12deg);
  }
  .hours-badge .time { font-size: 18px; }
  .hours-badge .to { font-size: 13px; }
  .lineup-band {
    position: absolute;
    left: 0; top: 578px; width: 536px; height: 122px;
    background: var(--flyer-black);
    text-align: center;
  }
  .lineup-intro {
    margin-top: 10px;
    color: var(--neon-yellow);
    font-size: 14px;
    font-weight: 500;
    letter-spacing: 0.03em;
  }
  .lineup-names {
    margin-top: 4px;
    color: var(--white);
    font-size: 22px;
    font-weight: 800;
    line-height: 1.2;
    white-space: nowrap;
  }
  .lineup-names .divider { color: var(--neon-green); padding: 0 6px; }
  .lineup-names .amp { color: var(--neon-yellow); }
  .venue-address {
    margin-top: 8px;
    color: var(--white);
    font-size: 11px;
    font-weight: 500;
    letter-spacing: 0.04em;
  }
</style>
</head>
<body>
  <main class="flyer">
    <div class="flame-field" role="img" aria-label="Photograph of roaring orange campfire flames"></div>

    <div class="brand">
      <span class="brand-mark"></span>
      <span class="brand-name">BRIARWOOD LOUNGE</span>
    </div>

    <svg class="event-title" viewBox="0 0 536 300" aria-label="Lantern Nights">
      <defs>
        <linearGradient id="flameFill" x1="0" y1="0" x2="0" y2="1">
          <stop offset="0" stop-color="#c2300a"/>
          <stop offset="0.5" stop-color="#ff7a12"/>
          <stop offset="1" stop-color="#ffd23a"/>
        </linearGradient>
      </defs>
      <text x="28" y="120" font-size="124" textLength="470" lengthAdjust="spacingAndGlyphs">Lantern</text>
      <text x="78" y="258" font-size="124" textLength="370" lengthAdjust="spacingAndGlyphs">Nights</text>
    </svg>

    <p class="event-tagline">GRAND OPENING EVENT</p>

    <div class="age-badge">21+</div>

    <div class="hours-badge">
      <span class="time">9PM</span>
      <span class="to">to</span>
      <span class="time">1:30AM</span>
    </div>

    <section class="lineup-band">
      <p class="lineup-intro">Pure House Music W/</p>
      <p class="lineup-names">DJ VORTEX<span class="divider">|</span>DJ MARCO TELLEN</p>
      <p class="lineup-names">DJ BRANDT <span class="amp">&amp;</span> DJ WOBNIX</p>
      <p class="venue-address">712 K AVENUE DAVIS CA</p>
    </section>

    <div class="flame-strip" role="img" aria-label="Photograph of a low band of bright flames"></div>
  </main>
</body>
</html>
```